Hello - we need a label design for our Quillon Health Hair Loss supplement. It is a natural hair loss supplement for black/african american women to regrow new hair and help restore hair loss & thinning hair due to vitamin deficiencies, traction alopecia, etc. It is a science based efficacious supplement with a centuries old medicinal herbal formula.
Attached is the logo & files of other generic competition and also Black hair products for your perusal. The label has to be a upscale and have an ethnic flair to it. The product is clinically effective, leveraged by Ancient Wisdom and Modern Science. The front of the label should include the following:
Quillon Health (logo)
Strand Revitalizer
Advanced Women’s Hair Loss Formula
TRACTION ALOPECIA THERAPY
- Prevents hair loss & restores thinning, fragile hair
- Promotes Natural Hair Growth
- Strengthens Hair for less breakage
- Visibly increases hair density & thickness
- Thicker, Stronger, Longer, Hydrated hair
- Promotes Follicle regeneration & Hair Growth
Site-Specific for hair loss & stunted growth
60 capsules 30-day supply
Target Market(s)
Black/African American Women
Look and feel

```html
<!DOCTYPE html>
<html lang="en">
<head>
<meta charset="utf-8">
<title>Quillon Health – Strand Revitalizer Label</title>
<link rel="stylesheet" href="https://fonts.googleapis.com/css2?family=Catamaran:wght@500;600;700;800&display=swap">
<style>
  :root {
    --page-bg: #ffffff;
    --label-bg: #1d1d1d;
    --bronze: #c8763a;
    --bronze-dark: #9a4f1f;
    --bronze-light: #d98a45;
    --band-text: #2b170a;
    --white: #ffffff;
    --rule: #d9d9d9;
  }
  * { box-sizing: border-box; margin: 0; padding: 0; }
  html, body {
    width: 1200px;
    height: 1000px;
    overflow: hidden;
    background: var(--page-bg);
    font-family: "Catamaran", "Helvetica Neue", Arial, sans-serif;
  }
  .label {
    position: absolute;
    left: 120px;
    top: 142px;
    width: 960px;
    height: 716px;
    background: var(--label-bg);
    color: var(--white);
  }
  .brand {
    position: absolute;
    top: 112px;
    left: 0;
    width: 100%;
    text-align: center;
    font-size: 38px;
    font-weight: 600;
    letter-spacing: 1px;
    color: var(--bronze-light);
  }
  .product-name {
    position: absolute;
    left: 275px;
    top: 219px;
    width: 420px;
    height: 61px;
    border-radius: 12px;
    background: linear-gradient(90deg, var(--bronze-dark), var(--bronze-light) 45%, var(--bronze) 70%, var(--bronze-dark));
    display: flex;
    align-items: center;
    justify-content: center;
    font-size: 34px;
    font-weight: 700;
    color: var(--white);
    white-space: nowrap;
  }
  .tagline {
    position: absolute;
    top: 302px;
    left: 0;
    width: 100%;
    text-align: center;
    font-size: 22px;
    font-weight: 700;
    line-height: 34px;
    text-transform: uppercase;
    letter-spacing: 0.3px;
  }
  .tagline-rule {
    position: absolute;
    top: 382px;
    left: 370px;
    width: 232px;
    height: 2px;
    background: var(--rule);
  }
  .benefit-band {
    position: absolute;
    top: 413px;
    left: 0;
    width: 100%;
    height: 207px;
  }
  .benefit-band-fill {
    position: absolute;
    inset: 0;
    background: linear-gradient(90deg, #a95a25, #c0692f 30%, #b9642c 60%, #a85826);
  }
  .benefit-list {
    position: absolute;
    inset: 0;
    list-style: none;
    padding-top: 14px;
    text-align: center;
    font-size: 21px;
    font-weight: 700;
    line-height: 27.5px;
    color: var(--band-text);
  }
  .benefit-list li::before { content: "·"; }
  .footer {
    position: absolute;
    left: 133px;
    top: 652px;
    width: 708px;
    height: 40px;
    border-bottom: 2px solid var(--rule);
    display: flex;
    justify-content: space-between;
    align-items: flex-end;
    padding-bottom: 2px;
  }
  .clinical {
    display: flex;
    align-items: flex-end;
    gap: 12px;
    font-size: 22px;
    font-weight: 700;
  }
  .clinical svg { width: 34px; height: 34px; }
  .supply {
    font-size: 22px;
    font-weight: 700;
  }
  .supply .count { font-size: 32px; font-weight: 800; }
</style>
</head>
<body>
  <main class="label">
    <div class="brand">Quillon Health</div>

    <div class="product-name">Strand Revitalizer</div>

    <p class="tagline">Advanced Women’s Hair Loss Formula<br>Traction Alopecia Therapy</p>
    <div class="tagline-rule"></div>

    <section class="benefit-band">
      <div class="benefit-band-fill" role="img" aria-label="Band of ethnic geometric pattern in bronze and rust tones"></div>
      <ul class="benefit-list">
        <li>Prevents hair loss &amp; restores thinning, fragile hair</li>
        <li>Promotes Natural Hair Growth</li>
        <li>Strengthens Hair for less breakage</li>
        <li>Visibly increases hair density &amp; thickness</li>
        <li>Thicker, Stronger, Longer, Hydrated hair</li>
        <li>Promotes Follicle regeneration &amp; Hair Growth</li>
      </ul>
    </section>

    <footer class="footer">
      <div class="clinical">
        <span>Clinically tested</span>
        <svg viewBox="0 0 34 34" aria-hidden="true">
          <g fill="none" stroke="#ffffff" stroke-width="1.8" stroke-linecap="round">
            <path d="M9 30 C9 20 12 12 15 4"/>
            <path d="M16 30 C16 20 19 12 22 5"/>
            <path d="M23 30 C23 22 26 15 29 9"/>
            <path d="M4 31 H31"/>
          </g>
        </svg>
      </div>
      <div class="supply"><span class="count">60</span> capsules &nbsp;30-day supply</div>
    </footer>
  </main>
</body>
</html>
```